New Real Estate business seek modern cutting edge stationery Design for Letterhead,Presentation fold

We need full stationary designs for new real estate company from Toronto Ontario. We would like a very cool, new, sleek, modern cutting edge design design for email signature, letterhead, envelope and presentation folder.

Let your imagination run wild, looking for a really cool package

Attached is all versions of my logo, the main colours are Red,white and black.

Industry/Entity Type

Real Estate

Requirements
Must have
• Envelope must have a Top secret stamp water marked into the middle
• Presentation folder must have SOLD sign inside
• Follow logo colour seem .
• make all txt editable

```html
<!DOCTYPE html>
<html lang="en">
<head>
<meta charset="utf-8">
<title>Northgate Realty Hub — Letterhead</title>
<link rel="stylesheet" href="https://fonts.googleapis.com/css2?family=Open+Sans:wght@400;600&display=swap">
<style>
  :root {
    --brand-red: #ed1c24;
    --ink-black: #000000;
    --paper: #ffffff;
    --fold-grey: #5a5a5a;
    --rule-grey-dark: #8c8c8c;
    --rule-grey-light: #e6e6e6;
    --social-blue: #3b5998;
    --social-red: #d4302b;
    --text-white: #ffffff;
  }
  * { margin: 0; padding: 0; box-sizing: border-box; }
  html, body { width: 850px; height: 1200px; overflow: hidden; background: var(--paper); }
  .letterhead {
    position: relative;
    width: 850px;
    height: 1200px;
    background: var(--paper);
    font-family: "Open Sans", Arial, sans-serif;
    overflow: hidden;
  }
  .brand {
    position: absolute;
    left: 70px;
    top: 80px;
    display: flex;
    align-items: center;
    gap: 12px;
  }
  .brand-mark {
    width: 80px;
    height: 80px;
    background: var(--brand-red);
  }
  .brand-text { display: flex; flex-direction: column; }
  .brand-name {
    font-size: 30px;
    line-height: 1.05;
    font-weight: 400;
    color: var(--ink-black);
    width: 190px;
  }
  .brand-tagline {
    margin-top: 6px;
    font-size: 7.5px;
    color: var(--ink-black);
  }
  .social {
    position: absolute;
    left: 22px;
    top: 1080px;
    display: flex;
    gap: 10px;
  }
  .social-square { width: 31px; height: 31px; border-radius: 3px; }
  .social-square.is-blue { background: var(--social-blue); }
  .social-square.is-red { background: var(--social-red); }
  .footer-rule {
    position: absolute;
    left: 0;
    top: 1121px;
    width: 850px;
    height: 9px;
    background: linear-gradient(180deg, var(--rule-grey-light), var(--rule-grey-dark));
  }
  .footer-band {
    position: absolute;
    left: 0;
    top: 1130px;
    width: 850px;
    height: 70px;
    background: var(--brand-red);
  }
  .contact {
    position: absolute;
    left: 24px;
    top: 1140px;
    color: var(--text-white);
    font-size: 16.5px;
    line-height: 26px;
  }
  .contact-line { display: flex; align-items: center; gap: 7px; }
  .contact-line svg { width: 16px; height: 14px; fill: var(--text-white); }
  .fold {
    position: absolute;
    left: 478px;
    top: 1082px;
    width: 360px;
    height: 118px;
  }
  .web-address {
    position: absolute;
    left: 478px;
    top: 1124px;
    width: 327px;
    text-align: center;
    color: var(--text-white);
    font-size: 21px;
    letter-spacing: 0.3px;
  }
</style>
</head>
<body>
  <main class="letterhead">
    <header class="brand">
      <div class="brand-mark"></div>
      <div class="brand-text">
        <span class="brand-name">Northgate Realty Hub</span>
        <span class="brand-tagline">Your trusted partner for every home move</span>
      </div>
    </header>

    <div class="social">
      <span class="social-square is-blue"></span>
      <span class="social-square is-red"></span>
    </div>

    <div class="footer-rule"></div>
    <div class="footer-band"></div>

    <svg class="fold" viewBox="0 0 360 118" aria-hidden="true">
      <polygon points="327,0 357,48 327,48" fill="var(--fold-grey)"/>
      <rect x="0" y="0" width="327" height="118" fill="var(--ink-black)"/>
    </svg>
    <p class="web-address">www.northgatehub.com</p>

    <address class="contact" style="font-style:normal">
      <div class="contact-line">
        <svg viewBox="0 0 16 14" aria-hidden="true">
          <path d="M1 4 Q8 -1 15 4 L13 6 L11 4.5 L5 4.5 L3 6 Z"/>
          <path d="M4 6 L12 6 L14 13 L2 13 Z"/>
        </svg>
        <span>555-014-2280</span>
      </div>
      <div class="contact-line">
        <svg viewBox="0 0 16 14" aria-hidden="true">
          <path d="M1 2 H15 V12 H1 Z M2 3 L8 8 L14 3" fill="none" stroke="var(--text-white)" stroke-width="1.3"/>
        </svg>
        <span>sam@northgatehub.com</span>
      </div>
    </address>
  </main>
</body>
</html>
```